National Female Non-profit Business Card

We need a business card design as soon as possible for a non-profit organisation called Meadow to Summit. Our aim is to empower leadership potential in rural female teens.
The business card should have our logo on the one side and then information on the other side, including name, job title, email address, phone number and website (www.meadowtosummit.com.au) and our twitter handle @MeadowSummit
It should use the colours white, coral (#f04a50) and orange (#f68e4e). The font used in the logo is Raleway.
The hashtag #YoungVoicesRise could be used.
It should be bright, chic and crisp. Our logo is attached.

Target Market(s)
We will be handing the cards out to politicians and senior executives. However, as we're a non-profit for young women, they also need to reflect femininity and youth.
Industry/Entity Type
Non-Profit
Look and feel

```html
<!DOCTYPE html>
<html lang="en">
<head>
<meta charset="utf-8">
<title>Meadow to Summit — Business Card</title>
<link rel="stylesheet" href="https://fonts.googleapis.com/css2?family=Raleway:wght@400&family=Roboto:wght@300;400;500&display=swap">
<style>
  :root {
    --backdrop: #eef0f3;
    --card: #ffffff;
    --coral: #f04a50;
    --orange: #f68e4e;
    --ink: #111111;
  }
  * { margin: 0; padding: 0; box-sizing: border-box; }
  html, body { width: 1200px; height: 1000px; overflow: hidden; }
  body {
    background: var(--backdrop);
    position: relative;
    font-family: "Roboto", Arial, sans-serif;
    color: var(--ink);
  }
  .card {
    position: absolute;
    top: 224px;
    width: 357px;
    height: 590px;
    background: var(--card);
    border-radius: 14px;
  }
  .card--front { left: 227px; }
  .card--back { left: 616px; }

  .brand-mark {
    position: absolute;
    left: 0; right: 0;
    top: 500px;
    text-align: center;
    font-family: "Raleway", Arial, sans-serif;
    font-weight: 400;
    font-size: 22px;
    letter-spacing: 0.2px;
    color: var(--coral);
  }
  .brand-mark__dot {
    display: block;
    width: 22px; height: 22px;
    margin: 0 auto 12px;
    border-radius: 50%;
    background: var(--coral);
  }

  .identity {
    position: absolute;
    left: 25px;
    top: 382px;
    padding-left: 20px;
    border-left: 5px solid var(--orange);
  }
  .identity__name {
    font-size: 19px;
    line-height: 22px;
    font-weight: 300;
    margin-top: -4px;
  }
  .identity__name strong { font-weight: 500; }
  .identity__role {
    font-size: 16px;
    line-height: 22px;
    font-weight: 300;
  }

  .contact-list {
    position: absolute;
    left: 18px;
    top: 468px;
    list-style: none;
  }
  .contact-list li {
    display: flex;
    align-items: center;
    height: 24.5px;
    font-size: 16px;
    font-weight: 300;
  }
  .contact-list svg {
    width: 20px; height: 20px;
    margin-right: 7px;
    flex: none;
  }
</style>
</head>
<body>

<section class="card card--front" aria-label="Card front">
  <div class="brand-mark">
    <span class="brand-mark__dot"></span>
    MEADOW TO SUMMIT
  </div>
</section>

<section class="card card--back" aria-label="Card back">
  <div class="identity">
    <p class="identity__name">Lena <strong>Hartwell</strong></p>
    <p class="identity__role">Director</p>
  </div>

  <ul class="contact-list">
    <li>
      <svg viewBox="0 0 20 20" aria-hidden="true">
        <circle cx="10" cy="10" r="8.5" fill="none" stroke="var(--orange)" stroke-width="1.4"/>
        <path d="M7.6 5.5 l2 1.2 -1 2.2 c.6 1.3 1.3 2 2.4 2.6 l1.6 -1.1 1.6 1.8 c-.6 1.4 -1.8 1.8 -3 1.2 c-2.2 -1.1 -3.9 -3 -4.6 -5.2 c-.3 -1.3 .1 -2.3 1 -2.7z" fill="var(--orange)"/>
      </svg>
      0400 555 012
    </li>
    <li>
      <svg viewBox="0 0 20 20" aria-hidden="true">
        <rect x="1" y="4" width="18" height="12" rx="1" fill="var(--orange)"/>
        <path d="M1.5 4.8 L10 11 L18.5 4.8" fill="none" stroke="#fff" stroke-width="1.4"/>
      </svg>
      contact@meadowtosummit.com.au
    </li>
    <li>
      <svg viewBox="0 0 20 20" aria-hidden="true">
        <circle cx="10" cy="10" r="7" fill="var(--orange)"/>
      </svg>
      MeadowSummit
    </li>
    <li>
      <svg viewBox="0 0 20 20" aria-hidden="true" fill="none" stroke="var(--orange)" stroke-width="1.2">
        <circle cx="10" cy="10" r="8.5"/>
        <ellipse cx="10" cy="10" rx="3.8" ry="8.5"/>
        <path d="M1.5 10 H18.5 M3 5.5 H17 M3 14.5 H17 M10 1.5 V18.5"/>
      </svg>
      meadowtosummit.com.au
    </li>
  </ul>
</section>

</body>
</html>
```